Auto and Home Insurance Quote Letter

I am an insurance agent and i have been mailing out a front back auto and home insurance quotes in black and white to prospects in my area. I would like the letter to be updated with a new look and some new graphics that would help catch the attention of the prospects I am mailing to. Anything that would help the prospect to call my office.

```html
<!DOCTYPE html>
<html lang="en">
<head>
<meta charset="utf-8">
<title>Wren Insurance Agency – Home Insurance Quote</title>
<link href="https://fonts.googleapis.com/css2?family=Poppins:wght@400;500;600;700;800&family=Source+Sans+3:wght@400;600;700&display=swap" rel="stylesheet">
<style>
  :root{
    --ink:#111111;
    --paper:#ffffff;
    --rule:#8a8a8a;
    --row-alt:#e8e8e8;
    --band:#4a4a4a;
    --muted:#555555;
    --white:#ffffff;
  }
  *{margin:0;padding:0;box-sizing:border-box;}
  html,body{width:848px;height:1200px;overflow:hidden;background:var(--paper);}
  .letter{position:relative;width:848px;height:1200px;color:var(--ink);font-family:"Source Sans 3",Arial,sans-serif;}
  .brand{position:absolute;top:130px;left:0;width:848px;text-align:center;font-family:"Poppins",Arial,sans-serif;font-weight:500;font-size:30px;letter-spacing:1px;color:var(--ink);}
  .rule-top{position:absolute;top:203px;left:16px;width:816px;height:1px;background:var(--rule);}
  .intro{position:absolute;top:228px;left:17px;width:815px;font-size:17.2px;line-height:23px;text-align:justify;color:#222;}
  .intro strong{font-weight:700;text-decoration:underline;}
  .example-title{position:absolute;top:308px;left:16px;width:816px;font-family:"Poppins",Arial,sans-serif;font-weight:700;font-size:20.5px;letter-spacing:-0.2px;white-space:nowrap;}
  .specs{position:absolute;top:374px;left:16px;width:816px;height:60px;border-top:1.5px solid var(--ink);border-bottom:1.5px solid var(--ink);display:flex;align-items:center;justify-content:center;font-family:"Poppins",Arial,sans-serif;font-weight:700;font-size:27px;letter-spacing:-0.3px;}
  .coverage{position:absolute;top:473px;left:16px;width:509px;border-collapse:collapse;font-size:16.5px;}
  .coverage th{background:var(--ink);color:var(--white);font-family:"Poppins",Arial,sans-serif;font-weight:600;font-size:16px;text-align:left;height:42px;}
  .coverage td{height:41.4px;color:#222;}
  .coverage tr:nth-child(even) td{background:var(--row-alt);}
  .coverage th:first-child,.coverage td:first-child{padding-left:43px;width:319px;}
  .premium{position:absolute;top:462px;left:525px;width:307px;height:384px;background:var(--paper);box-shadow:-2px 2px 8px rgba(0,0,0,.18);display:flex;flex-direction:column;align-items:center;justify-content:center;text-align:center;}
  .premium-label{font-family:"Poppins",Arial,sans-serif;font-size:26px;line-height:30px;font-weight:400;}
  .premium-amount{font-family:"Poppins",Arial,sans-serif;font-weight:700;font-size:54px;line-height:70px;margin-top:6px;}
  .disclaimer{position:absolute;top:869px;left:17px;width:815px;font-size:17.2px;line-height:23px;text-align:justify;color:#222;}
  .signoff{position:absolute;top:934px;left:16px;width:290px;}
  .signoff-greeting{font-family:"Poppins",Arial,sans-serif;font-weight:700;font-size:27px;}
  .signature{display:block;width:235px;height:60px;margin:10px 0 0 6px;background:linear-gradient(90deg,#e6e6e6,#f6f6f6);}
  .signer-name{margin:12px 0 0 10px;font-family:"Poppins",Arial,sans-serif;font-weight:800;font-size:21px;line-height:23px;}
  .signer-title{margin-left:10px;font-family:"Poppins",Arial,sans-serif;font-weight:800;font-size:21px;line-height:23px;color:var(--muted);}
  .divider-shadow{position:absolute;top:940px;left:304px;width:4px;height:150px;background:linear-gradient(90deg,rgba(0,0,0,.08),rgba(0,0,0,0));}
  .roof-offer{position:absolute;top:939px;left:374px;width:458px;height:156px;border-top:2px solid var(--band);border-left:2px solid var(--band);text-align:center;}
  .roof-title{margin-top:12px;font-family:"Poppins",Arial,sans-serif;font-weight:800;font-size:25px;letter-spacing:-0.5px;line-height:30px;}
  .roof-text{margin-top:2px;font-family:"Poppins",Arial,sans-serif;font-size:15.2px;line-height:23px;}
  .cta{position:absolute;left:-2px;bottom:0;width:458px;height:59px;background:var(--band);color:var(--white);font-family:"Poppins",Arial,sans-serif;font-weight:800;font-size:40px;letter-spacing:-0.5px;display:flex;align-items:center;justify-content:center;}
  .footer{position:absolute;top:1132px;left:16px;width:816px;height:53px;background:var(--band);color:var(--white);font-family:"Poppins",Arial,sans-serif;font-weight:700;font-size:20px;display:flex;align-items:center;padding-left:2px;padding-right:110px;white-space:nowrap;overflow:hidden;}
  .footer svg{flex:none;}
  .footer .item{display:flex;align-items:center;gap:4px;}
  .footer .sep{margin:0 7px;}
  .footer-mark{position:absolute;top:1112px;left:738px;width:92px;height:92px;border-radius:50%;background:var(--paper);border:3px solid var(--band);}
</style>
</head>
<body>
<div class="letter">
  <div class="brand">WREN INSURANCE AGENCY</div>
  <div class="rule-top"></div>

  <p class="intro">If you are tired of paying too much for Home Insurance and want <strong>all your insurance needs handled under one agency</strong>, then call us at <strong>555-018-2740</strong>. One call is all it takes to see if you’ve got the right coverage at the right price.</p>

  <h2 class="example-title">BELOW IS AN EXAMPLE OF A RECENT HOME INSURANCE POLICY IN LAKEPORT</h2>

  <div class="specs">YEAR BUILT: 2015 • 4 BEDROOMS • HEATED SQUARE FEET:</div>

  <table class="coverage">
    <thead><tr><th>COVERAGE</th><th>LIMIT</th></tr></thead>
    <tbody>
      <tr><td>A - Dwelling Protection</td><td>$305,000.00</td></tr>
      <tr><td>B - Other Structures</td><td>6,100.00</td></tr>
      <tr><td>C – Personal Property</td><td>106,750.00</td></tr>
      <tr><td>D – Loss of Use</td><td>30,500.00</td></tr>
      <tr><td>E - Personal Liability</td><td>$300,000</td></tr>
      <tr><td>F - Medical Protection</td><td>$1,000.00</td></tr>
      <tr><td>AOP Deductible</td><td>$2,500</td></tr>
      <tr><td>Hurricane Deductible</td><td>2%</td></tr>
    </tbody>
  </table>

  <div class="premium">
    <div class="premium-label">TOTAL ANNUAL<br>PREMIUM:</div>
    <div class="premium-amount">$725.00</div>
  </div>

  <p class="disclaimer">The quoted premium is a sample premium based on a recent policy purchased in Lakeport. Premium will differ based on information obtained on your application.</p>

  <div class="signoff">
    <div class="signoff-greeting">Sincerely,</div>
    <span class="signature" role="img" aria-label="Handwritten signature of the agency principal"></span>
    <div class="signer-name">DANIEL WHITMORE</div>
    <div class="signer-title">AGENCY PRINCIPAL</div>
  </div>
  <div class="divider-shadow"></div>

  <div class="roof-offer">
    <div class="roof-title">NEWER ROOF, SAVE EVEN MORE.</div>
    <div class="roof-text">If you have a newer roof, you may qualify for added<br>savings on your Harborline homeowners insurance.</div>
    <div class="cta">ASK ME TODAY!</div>
  </div>

  <div class="footer">
    <span class="item">
      <svg width="22" height="22" viewBox="0 0 24 24"><circle cx="12" cy="12" r="11" fill="#fff"/><path d="M8.2 6.5l2 2.6-1.2 1.6c.9 1.8 2.3 3.2 4.1 4.1l1.6-1.2 2.6 2-1.3 2c-4.6-.4-8.9-4.7-9.3-9.3z" fill="#4a4a4a"/></svg>555-018-2740
    </span>
    <span class="sep">•</span>
    <span class="item">
      <svg width="22" height="22" viewBox="0 0 24 24"><path d="M12 1.5a8 8 0 0 0-8 8c0 6 8 13 8 13s8-7 8-13a8 8 0 0 0-8-8z" fill="#fff"/><circle cx="12" cy="9.5" r="3.2" fill="#4a4a4a"/></svg>&nbsp;LAKEPORT, FL
    </span>
    <span class="sep">•</span>
    <span class="item">
      <svg width="22" height="22" viewBox="0 0 24 24" fill="none" stroke="#fff" stroke-width="1.6"><circle cx="12" cy="12" r="10"/><ellipse cx="12" cy="12" rx="4.5" ry="10"/><path d="M2 12h20M4 6.5h16M4 17.5h16"/></svg>&nbsp;&nbsp;WRENINSAGENCY.COM
    </span>
  </div>
  <div class="footer-mark"></div>
</div>
</body>
</html>
```